Business Card design for new private practice opening

I need a business card design for my new private practice with my new logo uploaded as a file
On the front the logo
On the back: maybe a small logo somewhere?
Priv. Doz. DDr. Corinna Vestaluk
Fachärztin für Allgemein- & Viszeralchirurgie
Address: xxx
Tel: xxx
Mobil:xxx
Webseite:xxx
Email:xxx

Contact Information for Business Card

See project description above for details

Requirements
Nice to have
• I would like the colors of the logo incorporated into the business card

```html
<!DOCTYPE html>
<html lang="de">
<head>
<meta charset="utf-8">
<title>Vestaluk Chirurgie – Visitenkarte</title>
<link rel="stylesheet" href="https://fonts.googleapis.com/css2?family=Lato:wght@400;700&display=swap">
<style>
  :root {
    --teal: #45b8b5;
    --grey: #7d7d7d;
    --ink: #2b2b2b;
    --line: #4a4a4a;
    --band-grey: #a0a0a0;
    --paper: #ffffff;
    --backdrop: #e6e7e9;
  }
  * { box-sizing: border-box; margin: 0; padding: 0; }
  html, body { width: 1200px; height: 900px; overflow: hidden; }
  body {
    background: var(--backdrop);
    font-family: "Lato", sans-serif;
    display: flex;
    flex-direction: column;
    align-items: center;
    justify-content: center;
    gap: 40px;
  }
  .card {
    position: relative;
    width: 680px;
    height: 388px;
    background: var(--paper);
    border-radius: 26px;
    overflow: hidden;
    box-shadow: 0 6px 20px rgba(0,0,0,.12);
  }

  /* Practice name with plain dot */
  .practice {
    display: flex;
    align-items: center;
  }
  .practice-dot {
    border-radius: 50%;
    background: var(--teal);
    flex: none;
  }
  .practice-name {
    font-family: "Lato", sans-serif;
    font-weight: 700;
    color: var(--grey);
    white-space: nowrap;
  }

  /* Front */
  .card--front {
    display: flex;
    align-items: center;
    justify-content: center;
  }
  .card--front .practice { gap: 26px; }
  .card--front .practice-dot { width: 84px; height: 84px; }
  .card--front .practice-name { font-size: 50px; }

  /* Back */
  .card--back .practice {
    position: absolute;
    top: 48px; right: 56px;
    gap: 12px;
  }
  .card--back .practice-dot { width: 30px; height: 30px; }
  .card--back .practice-name { font-size: 21px; }

  .holder {
    position: absolute;
    left: 48px; top: 182px;
  }
  .holder-accent {
    position: absolute;
    left: 0; top: 186px;
    width: 14px; height: 60px;
    background: var(--teal);
  }
  .holder-name {
    color: var(--teal);
    font-size: 32px;
    font-weight: 400;
    letter-spacing: .2px;
  }
  .holder-title {
    color: var(--grey);
    font-size: 19px;
    margin-top: 2px;
  }
  .divider {
    position: absolute;
    left: 48px; right: 48px; top: 262px;
    height: 1.5px;
    background: var(--line);
  }
  .contacts {
    position: absolute;
    left: 48px; right: 40px; top: 276px;
    display: grid;
    grid-template-columns: 1fr 1.25fr 1fr;
    column-gap: 20px;
    color: var(--ink);
    font-size: 17px;
  }
  .contact-list { list-style: none; display: flex; flex-direction: column; gap: 10px; }
  .contact-item { display: flex; align-items: center; gap: 10px; white-space: nowrap; }
  .contact-icon { width: 20px; height: 20px; flex: none; }
  .address { list-style: none; display: flex; flex-direction: column; gap: 10px; white-space: nowrap; }

  .footer-band {
    position: absolute;
    left: 0; right: 0; bottom: 0;
    height: 14px;
    display: flex;
  }
  .footer-band .band-teal { flex: 0 0 72%; background: var(--teal); }
  .footer-band .band-grey { flex: 1; background: var(--band-grey); }
</style>
</head>
<body>

  <section class="card card--front" aria-label="Vorderseite">
    <div class="practice">
      <span class="practice-dot" aria-hidden="true"></span>
      <span class="practice-name">Vestaluk Chirurgie</span>
    </div>
  </section>

  <section class="card card--back" aria-label="Rückseite">
    <div class="practice">
      <span class="practice-dot" aria-hidden="true"></span>
      <span class="practice-name">Vestaluk Chirurgie</span>
    </div>

    <span class="holder-accent" aria-hidden="true"></span>
    <div class="holder">
      <h1 class="holder-name">Priv. Doz. DDr. Corinna Vestaluk</h1>
      <p class="holder-title">Fachärztin für Allgemein- &amp; Viszeralchirurgie</p>
    </div>

    <div class="divider"></div>

    <div class="contacts">
      <ul class="contact-list">
        <li class="contact-item">
          <svg class="contact-icon" viewBox="0 0 24 24" aria-hidden="true"><path fill="#45b8b5" d="M6.6 10.8a15 15 0 0 0 6.6 6.6l2.2-2.2c.3-.3.7-.4 1-.2 1.1.4 2.3.6 3.6.6.6 0 1 .4 1 1V20c0 .6-.4 1-1 1A17 17 0 0 1 3 4c0-.6.4-1 1-1h3.5c.6 0 1 .4 1 1 0 1.3.2 2.5.6 3.6.1.3 0 .7-.2 1z"/></svg>
          044-123 456 789
        </li>
        <li class="contact-item">
          <svg class="contact-icon" viewBox="0 0 24 24" aria-hidden="true"><rect x="6" y="2" width="12" height="20" rx="2" fill="none" stroke="#45b8b5" stroke-width="2"/><circle cx="12" cy="18" r="1.2" fill="#45b8b5"/></svg>
          044-123 456 789
        </li>
      </ul>
      <ul class="contact-list">
        <li class="contact-item">
          <svg class="contact-icon" viewBox="0 0 24 24" aria-hidden="true"><rect x="2" y="5" width="20" height="14" rx="1" fill="#45b8b5"/><path d="M2 6l10 7 10-7" fill="none" stroke="#fff" stroke-width="1.6"/></svg>
          info@webname.com
        </li>
        <li class="contact-item">
          <svg class="contact-icon" viewBox="0 0 24 24" aria-hidden="true"><circle cx="12" cy="12" r="10" fill="#45b8b5"/><path d="M2 12h20M12 2c3 3 3 17 0 20M12 2c-3 3-3 17 0 20" fill="none" stroke="#fff" stroke-width="1.4"/></svg>
          www.websitename.com
        </li>
      </ul>
      <ul class="address">
        <li>421, Address line goes</li>
        <li>45452, Country name</li>
      </ul>
    </div>

    <div class="footer-band" aria-hidden="true">
      <span class="band-teal"></span>
      <span class="band-grey"></span>
    </div>
  </section>

</body>
</html>
```